Banner for construction site to identify developer

we need a 4 foot by 8 foot banner to hang on the fence of a residential townhome development in Phoenix, Arizona that identifies Tolvane Holdings as the company behind the development/project. Also needs to include the logo, phone number, and web address. Would like to stick with the blue colors provided in the attached logo. The blues should stay the same but the letters in the logo can change to another color if necessary. Feel free to use "Tolvane Holdings" in place of "Tolvane Holdings Group". Looking for use of colors/design to take up space so banner is not just text with a logo.

Target Market(s)

drive by traffic looking at the site

Industry/Entity Type

Real Estate

Colors
0054AA
0677BA
7BADD7
CADEEF
E8F1F8

Requirements
Must have
• company name, phone number and web address

```html
<!DOCTYPE html>
<html lang="en">
<head>
<meta charset="utf-8">
<title>Tolvane Holdings – Development Site Banner</title>
<link rel="stylesheet" href="https://fonts.googleapis.com/css2?family=Poppins:wght@500;600;700&display=swap">
<style>
  :root {
    --blue-deep: #1e6f9f;
    --blue-bright: #1ba7da;
    --ink: #3d3d3f;
    --white: #ffffff;
    --sky-light: #e8edf1;
    --sky-mid: #d7dde3;
    --page: #ffffff;
  }
  * { margin: 0; padding: 0; box-sizing: border-box; }
  html, body {
    width: 1200px; height: 1200px; overflow: hidden;
    background: var(--page);
    font-family: "Poppins", sans-serif;
  }
  .banner {
    position: absolute;
    left: 61px; top: 281px;
    width: 1085px; height: 543px;
    background: var(--blue-bright);
    box-shadow: 0 3px 6px rgba(0,0,0,0.25);
    overflow: hidden;
  }
  .banner__trim { position: absolute; left: 0; width: 100%; background: var(--blue-deep); }
  .banner__trim--top { top: 0; height: 14px; }
  .banner__trim--bottom { bottom: 0; height: 15px; }

  .hero {
    position: absolute; left: 0; top: 14px; width: 100%; height: 277px;
  }
  .hero__backdrop {
    position: absolute; inset: 0;
    background: linear-gradient(90deg, var(--sky-light) 0%, var(--sky-mid) 45%, #dfe4e9 75%, var(--sky-light) 100%);
  }
  .hero__location {
    position: absolute; right: 20px; top: 20px;
    font-size: 15px; font-weight: 600; letter-spacing: 1.5px;
    color: var(--ink);
  }
  .hero__name {
    position: absolute; left: 0; width: 100%; top: 140px;
    text-align: center;
    font-size: 84px; font-weight: 600; letter-spacing: -1.5px; line-height: 1;
    color: var(--ink);
    white-space: nowrap;
  }

  .title-band {
    position: absolute; left: 0; top: 291px; width: 100%; height: 81px;
    background: var(--blue-deep);
    display: flex; align-items: center; justify-content: center;
  }
  .title-band__text {
    font-size: 58px; font-weight: 700; letter-spacing: 19px;
    margin-right: -19px;
    color: var(--white); line-height: 1;
    white-space: nowrap;
  }
  .title-band__rule {
    position: absolute; left: 0; top: 387px; width: 100%; height: 3px;
    background: var(--blue-deep);
  }

  .contact {
    position: absolute; left: 0; width: 100%;
    text-align: center; color: var(--white);
    font-weight: 600; white-space: nowrap; line-height: 1;
  }
  .contact--phone { top: 407px; font-size: 35px; letter-spacing: 3px; }
  .contact--web { top: 462px; font-size: 35px; letter-spacing: 3.2px; }
  .contact__label { font-weight: 700; }
</style>
</head>
<body>
  <div class="banner">
    <div class="banner__trim banner__trim--top"></div>

    <section class="hero">
      <div class="hero__backdrop" role="img" aria-label="Faded photograph of a city skyline with high-rise buildings"></div>
      <p class="hero__location">Phoenix, Arizona</p>
      <h1 class="hero__name">Tolvane Holdings</h1>
    </section>

    <div class="title-band">
      <h2 class="title-band__text">DEVELOPMENT SITE</h2>
    </div>
    <div class="title-band__rule"></div>

    <p class="contact contact--phone"><span class="contact__label">PHONE:</span> (602) 555-0148</p>
    <p class="contact contact--web"><span class="contact__label">WEB:</span> WWW.TOLVANEHOLDINGSGROUP.COM</p>

    <div class="banner__trim banner__trim--bottom"></div>
  </div>
</body>
</html>
```